Smart, Classy, Conservative looking Legal Letterhead

I need a letterhead that when you look at it it "says to you " this is a well established law firm with very smart lawyers, which will one day be appearing before the Supreme Court of the USA. All information about the Law firm should appear at the top of the page. please no information in the footer.

Industry/Entity Type

Legal

Requirements
Must have
• The name of the law firm, both addresses, phone number and fax,, The names of the attorneys, the website.
• Fields that get changed such as the date, VIA, Address of who the letter is going to,
• Re, Index,
• should have a clean neat look, sleek
Nice to have
• some color would be nice. A logo of some sort could be nice as well. Maybe a single S or interlocking P's For Pelworth and Pelworth.
Should not have
• not too modern looking.

```html
<!DOCTYPE html>
<html lang="en">
<head>
<meta charset="utf-8">
<title>Pelworth &amp; Pelworth, LLC — Letterhead</title>
<link rel="stylesheet" href="https://fonts.googleapis.com/css2?family=Cinzel:wght@400;500&family=Questrial&display=swap">
<style>
  :root {
    --backdrop: #cbcbcb;
    --paper: #ffffff;
    --firm-blue: #14628f;
    --bar-grey: #a3a4a6;
    --ink: #2a2a2a;
    --ink-soft: #4a4a4a;
    --rule: #7a7a7a;
  }
  * { margin: 0; padding: 0; box-sizing: border-box; }
  html, body { width: 1200px; height: 1000px; overflow: hidden; }
  body {
    background: var(--backdrop);
    position: relative;
    font-family: "Questrial", "Century Gothic", sans-serif;
    color: var(--ink-soft);
  }
  .sheet {
    position: absolute;
    top: 185px;
    width: 487px;
    height: 630px;
    background: var(--paper);
  }
  .sheet--accent { left: 89px; }
  .sheet--plain { left: 625px; }

  .accent-band { position: absolute; top: 0; height: 8px; }
  .accent-band--blue { left: 0; width: 300px; background: var(--firm-blue); }
  .accent-band--grey { left: 304px; width: 183px; background: var(--bar-grey); }

  .masthead { position: absolute; left: 27px; top: 33px; }
  .sheet--plain .masthead { top: 25px; }

  .firm-mark {
    position: absolute; left: 0; top: 3px;
    width: 20px; height: 20px;
    background: var(--firm-blue);
  }
  .firm-name {
    position: absolute; left: 44px; top: 0;
    white-space: nowrap;
    font-family: "Cinzel", "Trajan Pro", serif;
    font-weight: 500;
    font-size: 13.5px;
    letter-spacing: 0.2px;
    color: var(--ink);
  }
  .firm-rule {
    position: absolute; left: 44px; top: 18px;
    width: 188px; height: 1px; background: var(--rule);
  }
  .firm-tagline {
    position: absolute; left: 44px; top: 20px;
    white-space: nowrap;
    font-family: "Cinzel", "Trajan Pro", serif;
    font-size: 8.5px;
    color: var(--ink);
  }

  .attorney-list {
    position: absolute; left: 29px; top: 76px;
    list-style: none;
    font-size: 5.6px;
    line-height: 7.9px;
    text-transform: uppercase;
    color: var(--ink-soft);
  }
  .sheet--plain .attorney-list { left: 30px; top: 68px; }
  .attorney-list .footnote { font-size: 4.4px; line-height: 8px; }

  .contact {
    position: absolute; right: 28px; top: 31px;
    text-align: right;
    font-size: 5.6px;
    line-height: 7.2px;
    color: var(--ink-soft);
  }
  .sheet--plain .contact { top: 23px; }
  .contact .label { color: var(--firm-blue); font-weight: bold; }
  .office-title {
    margin-top: 9px;
    color: var(--firm-blue);
    font-weight: bold;
    text-transform: uppercase;
  }
</style>
</head>
<body>

  <section class="sheet sheet--accent" aria-label="Letterhead with colour band">
    <div class="accent-band accent-band--blue"></div>
    <div class="accent-band accent-band--grey"></div>

    <header class="masthead">
      <span class="firm-mark"></span>
      <h1 class="firm-name">PELWORTH &amp; PELWORTH, LLC</h1>
      <span class="firm-rule"></span>
      <p class="firm-tagline">ATTORNEYS AT LAW</p>
    </header>

    <ul class="attorney-list">
      <li>Michael Pelworth, Esq.</li>
      <li>Daniel A. Pelworth, Esq.</li>
      <li>Elizabeth Harrowgate, Esq.</li>
      <li>Peter T. Marsh, Esq.*</li>
      <li class="footnote">*Admitted in NY &amp; MA</li>
    </ul>

    <address class="contact">
      48 Halden Street<br>
      New York, New York 10007<br>
      <span class="label">Tel:</span> 914-555-0142 - <span class="label">Fax:</span> 914-555-0187<br>
      <span class="label">Email:</span> Daniel.Pelworth@pelworthlegal.com<br>
      www.newyorkclientadvocates.com
      <div class="office-title">Westchester Office</div>
      217 Orchard Road<br>
      Brookvale<br>
      New York 10571
    </address>
  </section>

  <section class="sheet sheet--plain" aria-label="Letterhead without colour band">
    <header class="masthead">
      <span class="firm-mark"></span>
      <h1 class="firm-name">PELWORTH &amp; PELWORTH, LLC</h1>
      <span class="firm-rule"></span>
      <p class="firm-tagline">ATTORNEYS AT LAW</p>
    </header>

    <ul class="attorney-list">
      <li>Michael Pelworth, Esq.</li>
      <li>Daniel A. Pelworth, Esq.</li>
      <li>Elizabeth Harrowgate, Esq.</li>
      <li>Peter T. Marsh, Esq.*</li>
      <li class="footnote">*Admitted in NY &amp; MA</li>
    </ul>

    <address class="contact">
      48 Halden Street<br>
      New York, New York 10007<br>
      <span class="label">Tel:</span> 914-555-0142 - <span class="label">Fax:</span> 914-555-0187<br>
      <span class="label">Email:</span> Daniel.Pelworth@pelworthlegal.com<br>
      www.newyorkclientadvocates.com
      <div class="office-title">Westchester Office</div>
      217 Orchard Road<br>
      Brookvale<br>
      New York 10571
    </address>
  </section>

</body>
</html>
```